Business Card Design needed for start up company Pramora

In need of a new business card designed for a start up company based in Sydney, Pramora is a new start up innovative Company, our mission it to make property accessible for everyday Australian and to become the leading Real Estate platform in Australia. We want it to be fresh and clean.

Industry/Entity Type

Financial

Contact Information for Business Card

Section for Name
Section for Title

PRAMORA - Where Doors Open Wide
Mobile:
Direct:

Font styles to use
Sans Serif

Colors
33a6d7
0692cd
0255a3
ffffff

Requirements
Must have
• Logo, all business card details

```html
<!DOCTYPE html>
<html lang="en">
<head>
<meta charset="utf-8">
<title>Pramora Business Card</title>
<link href="https://fonts.googleapis.com/css2?family=Lato:wght@400;700;900&display=swap" rel="stylesheet">
<style>
  :root {
    --page-bg: #e3e1de;
    --card-top: #f4f6f8;
    --card-bottom: #e6ebf0;
    --navy: #0f2a55;
    --brand-blue: #0255a3;
    --mid-blue: #0692cd;
    --sky-blue: #33a6d7;
    --icon-blue: #1c5d8e;
    --faint-circle: rgba(51, 166, 215, 0.14);
    --white: #ffffff;
  }
  * { box-sizing: border-box; margin: 0; padding: 0; }
  html, body {
    width: 1200px;
    height: 970px;
    overflow: hidden;
    background: var(--page-bg);
    font-family: "Lato", sans-serif;
  }
  .card {
    position: absolute;
    left: 50px;
    top: 173px;
    width: 1100px;
    height: 624px;
    border-radius: 32px;
    overflow: hidden;
    background: linear-gradient(160deg, var(--card-top), var(--card-bottom));
    box-shadow: 0 10px 30px rgba(0, 0, 0, 0.12);
  }
  .decor-circle {
    position: absolute;
    left: -10px;
    top: -150px;
    width: 480px;
    height: 480px;
    border-radius: 50%;
    background: var(--faint-circle);
  }
  .holder {
    position: absolute;
    left: 58px;
    top: 76px;
  }
  .holder-name {
    font-weight: 900;
    font-size: 38px;
    color: var(--navy);
    letter-spacing: -0.5px;
    line-height: 1;
  }
  .holder-title {
    font-weight: 400;
    font-size: 27px;
    color: var(--brand-blue);
    margin-top: 4px;
  }
  .brand {
    position: absolute;
    right: 52px;
    top: 52px;
    text-align: right;
  }
  .brand-row {
    display: flex;
    align-items: center;
    gap: 18px;
  }
  .brand-dot {
    width: 74px;
    height: 74px;
    border-radius: 50%;
    background: var(--brand-blue);
  }
  .brand-name {
    font-weight: 900;
    font-size: 78px;
    color: var(--navy);
    letter-spacing: -1px;
    line-height: 1;
  }
  .brand-tagline {
    font-weight: 700;
    font-size: 25px;
    color: var(--navy);
    letter-spacing: 0.5px;
    margin-top: 10px;
  }
  .contacts {
    position: absolute;
    left: 60px;
    top: 388px;
    list-style: none;
  }
  .contacts li {
    display: flex;
    align-items: center;
    gap: 12px;
    height: 40px;
    font-size: 30px;
    color: var(--navy);
  }
  .contact-icon { width: 34px; height: 34px; flex: none; }
  .address {
    position: absolute;
    right: 52px;
    top: 440px;
    text-align: right;
    font-size: 28px;
    line-height: 34px;
    color: var(--navy);
  }
  .wave {
    position: absolute;
    left: 0;
    bottom: 0;
    width: 1100px;
    height: 140px;
  }
</style>
</head>
<body>
  <div class="card">
    <div class="decor-circle"></div>

    <div class="holder">
      <p class="holder-name">LIAM HARTLEY</p>
      <p class="holder-title">Owner</p>
    </div>

    <div class="brand">
      <div class="brand-row">
        <span class="brand-dot"></span>
        <span class="brand-name">PRAMORA</span>
      </div>
      <p class="brand-tagline">Where Doors Open Wide</p>
    </div>

    <ul class="contacts">
      <li>
        <svg class="contact-icon" viewBox="0 0 34 34" aria-hidden="true">
          <circle cx="17" cy="17" r="17" fill="var(--icon-blue)"/>
          <rect x="12" y="8" width="10" height="18" rx="2" fill="none" stroke="#fff" stroke-width="2"/>
          <line x1="15" y1="23" x2="19" y2="23" stroke="#fff" stroke-width="1.6"/>
        </svg>
        <span>0412 555 078</span>
      </li>
      <li>
        <svg class="contact-icon" viewBox="0 0 34 34" aria-hidden="true">
          <circle cx="17" cy="17" r="17" fill="var(--icon-blue)"/>
          <path d="M8 14 Q17 7 26 14 L23 16 L20 13 L14 13 L11 16 Z" fill="#fff"/>
          <rect x="10" y="17" width="14" height="8" rx="1.5" fill="#fff"/>
        </svg>
        <span>02 9555 0143</span>
      </li>
      <li>
        <svg class="contact-icon" viewBox="0 0 34 34" aria-hidden="true">
          <circle cx="17" cy="17" r="17" fill="var(--icon-blue)"/>
          <rect x="9" y="11" width="16" height="12" fill="none" stroke="#fff" stroke-width="1.8"/>
          <path d="M9 11 L17 18 L25 11" fill="none" stroke="#fff" stroke-width="1.8"/>
        </svg>
        <span>liam@pramora.com.au</span>
      </li>
    </ul>

    <div class="address">
      <p>PO BOX 418 Harbour Street</p>
      <p>Sydney NSW 2000, Australia</p>
    </div>

    <svg class="wave" viewBox="0 0 1100 140" preserveAspectRatio="none" aria-hidden="true">
      <path d="M0 8 C220 60 460 86 660 80 C850 74 980 32 1100 10 L1100 24 C980 46 850 88 660 94 C460 100 220 74 0 24 Z" fill="var(--mid-blue)"/>
      <path d="M0 38 C220 84 460 108 660 102 C850 96 980 56 1100 34 L1100 140 L0 140 Z" fill="var(--navy)"/>
      <path d="M0 32 C220 78 460 102 660 96 C850 90 980 50 1100 28" fill="none" stroke="var(--white)" stroke-width="4"/>
    </svg>
  </div>
</body>
</html>
```